Design a web site for my business - Brellan Coatworks Mackaby.

We are a family business that handles design, fabrication and installation of powder coated aluminum, stainless steel and glass products. Including handrails, privacy slat screens, electric gates and pool fencing. We are based in the Whitsundays in North Queensland and service an area from Airlie Beach to Townsville.

Target Market(s)

Domestic and commercial

Industry/Entity Type

fabrication - manufacturing

Coding

Coded - Design and coding required

Number of Pages Required

5+ page

Colors
0054AA
0677BA
7BADD7
CADEEF
E8F1F8

Requirements
Must have
• photo galleries, contact page, one page for privacy screens, balustrades, glass fencing, stainless steel handrail, powder coated aluminium handrails and pool fencing

```html
<!DOCTYPE html>
<html lang="en">
<head>
<meta charset="utf-8">
<title>Brellan Coatworks Mackaby</title>
<link href="https://fonts.googleapis.com/css2?family=Poppins:wght@400;500;600;700&display=swap" rel="stylesheet">
<style>
:root{
  --navy:#0a1f4f;
  --navy-deep:#0b1a3a;
  --blue:#0054AA;
  --blue-mid:#0677BA;
  --blue-soft:#7BADD7;
  --blue-pale:#CADEEF;
  --blue-wash:#E8F1F8;
  --ink:#1c2433;
  --white:#fff;
}
*{box-sizing:border-box;margin:0;padding:0}
html,body{width:1200px;height:2890px;overflow:hidden}
body{font-family:'Poppins',sans-serif;color:var(--ink);background:#fff}
.page{position:relative;width:1200px;height:2890px}
section,header,footer,div{position:relative}
svg{display:inline-block;vertical-align:middle}
.btn{display:inline-flex;align-items:center;gap:10px;font-weight:600;font-size:12px;border-radius:3px;padding:0 17px;height:36px;white-space:nowrap}
.btn-blue{background:var(--blue);color:#fff}
.btn-outline-light{border:1px solid #fff;color:#fff}
.btn-white{background:#fff;color:var(--blue)}
.btn-outline-blue{border:1px solid var(--blue);color:var(--blue)}
.eyebrow{font-size:13px;font-weight:600;color:var(--blue);letter-spacing:.2px}
.rule{width:36px;height:2px;background:var(--blue)}

/* top bar */
.topbar{height:36px;background:var(--navy);color:#fff;font-size:11px;display:flex;align-items:center;padding:0 34px}
.topbar .contact{margin-left:auto;display:flex;gap:22px;align-items:center}
.topbar .contact span{display:flex;gap:6px;align-items:center}
.square-mark{width:13px;height:13px;background:#fff;border-radius:2px}

/* nav */
.nav{height:71px;display:flex;align-items:center;padding:0 35px;background:#fff;box-shadow:0 1px 3px rgba(0,0,0,.06)}
.brand{display:flex;align-items:center;gap:8px;font-weight:600;font-size:12px;color:#5a6170;width:160px;line-height:1.2}
.brand .dot{width:30px;height:30px;border-radius:50%;background:#5a6170;flex:none}
.menu{display:flex;gap:46px;margin-left:230px;font-size:13px;font-weight:500}
.menu .on{color:var(--blue)}
.nav .btn{margin-left:auto;background:var(--navy);color:#fff;height:37px;padding:0 27px;border-radius:3px}

/* hero */
.hero{height:521px;background:linear-gradient(100deg,#1f2a24 0%,#2d3b30 35%,#53625a 60%,#7c8b84 80%,#4c6b3c 100%);color:#fff;overflow:hidden}
.hero .photo{position:absolute;inset:0}
.hero .shade{position:absolute;inset:0;background:linear-gradient(90deg,rgba(15,22,18,.75),rgba(15,22,18,.2) 65%,rgba(0,0,0,0))}
.hero h3{position:absolute;left:35px;top:36px;font-size:17px;font-weight:600}
.hero h1{position:absolute;left:33px;top:64px;font-size:46px;font-weight:700;letter-spacing:.5px}
.hero h1 em{font-style:normal;color:var(--blue-soft)}
.hero .rule{position:absolute;left:35px;top:133px;width:58px;background:var(--blue-soft)}
.hero p{position:absolute;left:35px;top:163px;width:400px;font-size:14px;line-height:25px}
.hero .ctas{position:absolute;left:35px;top:303px;display:flex;gap:16px}
.hero .ctas .btn{height:37px}
.features{position:absolute;left:35px;top:429px;display:flex}
.feature{display:flex;gap:12px;padding-right:18px;margin-right:18px;border-right:1px solid rgba(255,255,255,.6);height:46px}
.feature:last-child{border:none}
.feature b{display:block;font-size:11px;font-weight:600}
.feature small{display:block;font-size:10px;line-height:15px;opacity:.9;margin-top:3px}
.locbox{position:absolute;left:949px;top:392px;width:233px;height:84px;background:rgba(10,31,79,.92);border-radius:3px;display:flex;gap:14px;padding:14px 16px}
.locbox b{font-size:12px;font-weight:500}
.locbox small{display:block;font-size:10px;line-height:18px;margin-top:4px}

/* products */
.products{height:378px;background:#fff}
.products .intro{position:absolute;left:34px;top:44px;width:270px}
.products h2{font-size:19px;font-weight:700;color:var(--navy);line-height:24px;margin-top:12px}
.products .intro .rule{margin:18px 0 16px}
.products .intro p{font-size:13px;line-height:25px;width:272px}
.products .intro .btn{margin-top:23px;height:36px}
.card{position:absolute;top:39px;width:250px;height:300px;border:1px solid #e2e6ec;border-radius:3px;text-align:center;background:#fff}
.card .img{height:154px}
.card h4{font-size:13px;font-weight:600;color:var(--navy);margin-top:17px}
.card p{font-size:12px;line-height:20px;margin:8px auto 0;width:170px}
.card .more{font-size:12px;font-weight:600;color:var(--blue);margin-top:8px;display:flex;gap:8px;justify-content:center;align-items:center}

/* stats */
.stats{height:138px;background:linear-gradient(90deg,#5d6b70,#8e9da3 50%,#3f4f4c);overflow:hidden}
.stats .panel{position:absolute;left:0;top:0;width:785px;height:138px;background:var(--navy);clip-path:polygon(0 0,100% 0,93% 100%,0 100%)}
.stat{position:absolute;top:20px;color:#fff}
.stat .big{font-size:25px;font-weight:600;line-height:28px}
.stat b{display:block;font-size:11px;font-weight:600;color:var(--blue-soft);margin-top:2px}
.stat small{display:block;font-size:12px;line-height:17px;margin-top:4px}
.stat-div{position:absolute;top:28px;width:1px;height:84px;background:rgba(255,255,255,.45)}
.stats .cta{position:absolute;left:846px;top:26px;color:#fff}
.stats .cta h3{font-size:16px;font-weight:600}
.stats .cta p{font-size:10px;margin-top:2px}
.stats .cta .row{display:flex;gap:17px;margin-top:14px}

/* serving */
.serving{height:138px;background:var(--blue-wash);text-align:center}
.serving h5{font-size:12px;font-weight:600;color:var(--navy);padding-top:40px}
.serving .row{display:flex;justify-content:center;gap:30px;margin-top:18px;font-size:8px;color:#394458;align-items:center}
.serving .row span{display:flex;gap:6px;align-items:center;white-space:nowrap}
.plain-tri{width:0;height:0;border-left:13px solid transparent;border-right:13px solid transparent;border-bottom:24px solid var(--navy)}
.wordmark{font-weight:700;font-size:15px;color:var(--navy);line-height:1;text-align:left}
.wordmark small{display:block;font-size:8px;font-weight:400;color:var(--blue-mid);margin-top:2px}
.serving .row .wordmark{display:block}

/* about */
.about{height:268px;background:linear-gradient(90deg,#fff 0%,#fff 35%,#d9dfdc 50%,#7f8d83 65%,#5d6d59 80%,#8a9891 100%);overflow:hidden}
.about .intro{position:absolute;left:34px;top:28px;width:440px}
.about h2{font-size:19px;font-weight:700;color:var(--navy);line-height:24px;margin-top:6px}
.about h2 em{font-style:normal;color:var(--blue)}
.about .rule{margin:16px 0 18px}
.about p{font-size:12.5px;line-height:20px;margin-bottom:12px}
.about .btn{position:absolute;left:844px;top:200px;height:37px}

/* process */
.process{height:342px;background:var(--navy);color:#fff;text-align:center}
.process h5{font-size:13px;font-weight:600;padding-top:52px}
.process h2{font-size:19px;font-weight:600;margin-top:8px}
.steps{position:absolute;top:134px;left:0;width:1200px}
.step{position:absolute;width:210px;margin-left:-105px}
.step .ring{width:67px;height:67px;border-radius:50%;border:1.5px solid rgba(255,255,255,.85);margin:0 auto;display:flex;align-items:center;justify-content:center}
.step .num{width:26px;height:26px;border-radius:50%;background:#fff;color:var(--navy);font-size:11px;font-weight:700;display:flex;align-items:center;justify-content:center;margin:-16px auto 0;position:relative}
.step h4{font-size:15px;font-weight:600;margin-top:12px}
.step p{font-size:12px;line-height:20px;margin-top:10px}

/* vision */
.vision{height:313px;background:linear-gradient(90deg,var(--blue-wash) 0%,var(--blue-wash) 45%,#dbe4ea 70%,#9fb1b3 100%);overflow:hidden}
.vision .intro{position:absolute;left:33px;top:42px;width:375px}
.vision h2{font-size:19px;font-weight:700;color:var(--navy);line-height:24px}
.vision h2 em{font-style:normal;color:var(--blue)}
.vision .rule{margin:14px 0 18px}
.vision p{font-size:12.5px;line-height:20px}
.vision .btns{position:absolute;left:666px;top:96px;display:flex;gap:24px}
.vision .btns .btn{height:45px;width:203px;justify-content:center;font-size:15px;gap:14px}
.vision .btn-outline-blue{background:rgba(255,255,255,.2)}
.perks{position:absolute;left:617px;top:221px;display:flex;align-items:center;font-size:13px;font-weight:600;color:var(--navy);white-space:nowrap}
.perks span{display:flex;align-items:center;gap:9px}
.perks i{width:2px;height:27px;background:var(--blue);margin:0 22px}

/* footer */
.footer{height:548px;background:var(--navy-deep);color:#fff}
.footer .col{position:absolute;top:50px}
.fdiv{position:absolute;top:50px;width:1px;height:454px;background:rgba(255,255,255,.2)}
.fbrand{font-size:15px;font-weight:700;line-height:20px;display:flex;gap:8px;align-items:center;white-space:nowrap}
.fbrand .dot{width:30px;height:30px;border-radius:50%;background:#fff;flex:none}
.fbrand small{display:block;font-size:13px;font-weight:400;color:var(--blue-soft);letter-spacing:1px}
.footer .rule{background:var(--blue-mid);margin:26px 0 26px}
.footer p{font-size:12px;line-height:25px}
.footer h4{font-size:15px;font-weight:600;letter-spacing:.3px}
.flinks{margin-top:40px;width:240px}
.flinks li{list-style:none;font-size:12px;display:flex;justify-content:space-between;padding-bottom:14px;margin-bottom:14px;border-bottom:1px solid rgba(255,255,255,.2)}
.map{width:230px;height:250px;margin-top:20px;background:radial-gradient(ellipse at 55% 55%,#1c3d7a 0%,#13295a 45%,var(--navy-deep) 75%)}
.fcontact li{list-style:none;display:flex;gap:14px;align-items:center;font-size:12px;margin-bottom:25px}
.socials{display:flex;gap:20px;margin-top:26px}
.socials i{width:20px;height:20px;border:2px solid #fff;border-radius:3px}

.badges{height:84px;background:#fff;display:flex;align-items:center;justify-content:center;font-size:11px;color:var(--navy)}
.badges span{display:flex;align-items:center;gap:10px;padding:0 22px;border-right:1px solid #9fb0c6;height:30px;white-space:nowrap}
.badges span:last-child{border:none}
.badges .wordmark{display:block;height:auto}
.copy{height:53px;background:#fff;border-top:1px solid #eef1f5;font-size:11px;color:#394458;display:flex;align-items:center;padding:0 50px}
.copy .links{margin-left:175px;display:flex;gap:24px}
.copy .links i{width:1px;height:14px;background:#394458}
</style>
</head>
<body>
<div class="page">

<div class="topbar">
  <span>Proudly based in the Whitsundays, North Queensland</span>
  <div class="contact">
    <span><svg width="12" height="12" viewBox="0 0 24 24"><path fill="#fff" d="M6.6 10.8a15 15 0 006.6 6.6l2.2-2.2c.3-.3.7-.4 1-.2 1.1.4 2.3.6 3.6.6.6 0 1 .4 1 1V20c0 .6-.4 1-1 1A17 17 0 013 4c0-.6.4-1 1-1h3.5c.6 0 1 .4 1 1 0 1.3.2 2.5.6 3.6.1.3 0 .7-.2 1z"/></svg>0400 555 018</span>
    <span><svg width="13" height="10" viewBox="0 0 26 20"><rect x="1" y="1" width="24" height="18" rx="2" fill="none" stroke="#fff" stroke-width="2"/><path d="M1 2l12 9 12-9" fill="none" stroke="#fff" stroke-width="2"/></svg>info@brellancoatworks.com.au</span>
    <i class="square-mark"></i>
  </div>
</div>

<header class="nav">
  <div class="brand"><span class="dot"></span>Brellan Coatworks Mackaby</div>
  <nav class="menu"><span class="on">Home</span><span>About Us</span><span>ProductsGallery</span><span>Projects</span><span>Contact</span></nav>
  <span class="btn">Get a Quote</span>
</header>

<section class="hero">
  <div class="photo" role="img" aria-label="Frameless glass pool fence beside a stone wall with tropical garden"></div>
  <div class="shade"></div>
  <h3>QUALITY FABRICATION.</h3>
  <h1>BUILT TO <em>LAST.</em></h1>
  <div class="rule"></div>
  <p>Specialising in powder coated aluminium, stainless steel and glass solutions for homes and businesses across the Whitsundays and North Queensland.</p>
  <div class="ctas">
    <span class="btn btn-blue">Our Products <svg width="13" height="10" viewBox="0 0 14 10"><path d="M0 5h12M8 1l4 4-4 4" stroke="#fff" fill="none" stroke-width="1.5"/></svg></span>
    <span class="btn btn-outline-light">Our Products <svg width="13" height="10" viewBox="0 0 14 10"><path d="M0 5h12M8 1l4 4-4 4" stroke="#fff" fill="none" stroke-width="1.5"/></svg></span>
  </div>
  <div class="features">
    <div class="feature"><svg width="26" height="26" viewBox="0 0 26 26"><circle cx="13" cy="13" r="11" fill="none" stroke="var(--blue-soft)" stroke-width="1.5"/><path d="M8 13l3.5 3.5L18 10" fill="none" stroke="var(--blue-soft)" stroke-width="1.5"/></svg><div><b>PREMIUM QUALITY</b><small>Top grade materials<br>built to last.</small></div></div>
    <div class="feature"><svg width="26" height="26" viewBox="0 0 26 26"><rect x="3" y="6" width="20" height="14" rx="2" fill="none" stroke="var(--blue-soft)" stroke-width="1.5"/><path d="M3 11h20M3 15h20" stroke="var(--blue-soft)" stroke-width="1.2"/></svg><div><b>CUSTOM FABRICATION</b><small>Tailored solutions to<br>suit your project.</small></div></div>
    <div class="feature"><svg width="26" height="26" viewBox="0 0 26 26"><path d="M3 12L13 4l10 8v11H16v-7h-6v7H3z" fill="none" stroke="var(--blue-soft)" stroke-width="1.5"/></svg><div><b>DOMESTIC &amp; COMMERCIAL</b><small>Proudly serving homes<br>and businesses.</small></div></div>
    <div class="feature"><svg width="26" height="26" viewBox="0 0 26 26"><circle cx="12" cy="8" r="5" fill="none" stroke="var(--blue-soft)" stroke-width="1.5"/><path d="M3 24c0-6 4-9 9-9s9 3 9 9" fill="none" stroke="var(--blue-soft)" stroke-width="1.5"/></svg><div><b>LOCAL EXPERTS</b><small>Based in the Whitsundays,<br>servicing North Queensland.</small></div></div>
  </div>
  <div class="locbox">
    <svg width="20" height="26" viewBox="0 0 20 26"><path d="M10 1a8 8 0 018 8c0 6-8 16-8 16S2 15 2 9a8 8 0 018-8z" fill="var(--blue-soft)"/><circle cx="10" cy="9" r="3" fill="var(--navy)"/></svg>
    <div><b>Local to the Whitsundays</b><small>Servicing from Airlie Beach to Townsville and surrounding areas.</small></div>
  </div>
</section>

<section class="products">
  <div class="intro">
    <div class="eyebrow">OUR PRODUCTS</div>
    <h2>FUNCTIONAL.<br>STYLISH. BUILT<br>FOR QUEENSLAND.</h2>
    <div class="rule"></div>
    <p>From concept to completion, we deliver high-quality custom-made solutions using premium materials and expert craftsmanship.</p>
    <span class="btn btn-blue">View All Products <svg width="13" height="10" viewBox="0 0 14 10"><path d="M0 5h12M8 1l4 4-4 4" stroke="#fff" fill="none" stroke-width="1.5"/></svg></span>
  </div>
  <div class="card" style="left:333px"><div class="img" role="img" aria-label="Cream aluminium slat privacy screen and gate" style="background:linear-gradient(180deg,#9fb6cf 0%,#d8d3c8 40%,#c9c2b4 100%)"></div><h4>PRIVACY SCREENS</h4><p>Powder coated aluminium slat screens for privacy, security and style.</p><div class="more">VIEW MORE <svg width="13" height="10" viewBox="0 0 14 10"><path d="M0 5h12M8 1l4 4-4 4" stroke="var(--blue)" fill="none" stroke-width="1.5"/></svg></div></div>
  <div class="card" style="left:615px"><div class="img" role="img" aria-label="Timber deck with glass balustrade over garden" style="background:linear-gradient(180deg,#3a2f28 0%,#6b5a4a 45%,#8a9a8a 75%,#4f6a3a 100%)"></div><h4>GLASS FENCING</h4><p>Sleek, safe and compliant glass pool fencing solutions.</p><div class="more">VIEW MORE <svg width="13" height="10" viewBox="0 0 14 10"><path d="M0 5h12M8 1l4 4-4 4" stroke="var(--blue)" fill="none" stroke-width="1.5"/></svg></div></div>
  <div class="card" style="left:899px"><div class="img" role="img" aria-label="Boardwalk with stainless steel handrail through bushland" style="background:linear-gradient(160deg,#4a6a3a 0%,#7a6a5a 50%,#5a7a45 100%)"></div><h4>STAINLESS STEEL HANDRAILS</h4><p>Durable stainless steel handrails for a premium finish.</p><div class="more">VIEW MORE <svg width="13" height="10" viewBox="0 0 14 10"><path d="M0 5h12M8 1l4 4-4 4" stroke="var(--blue)" fill="none" stroke-width="1.5"/></svg></div></div>
</section>

<section class="stats" role="img" aria-label="Stainless handrail along a coastal walkway">
  <div class="panel"></div>
  <div class="stat" style="left:32px"><div class="big">15+</div><b>YEARS EXPERIENCE</b><small>Delivering quality<br>solutions since<br>2009.</small></div>
  <div class="stat-div" style="left:179px"></div>
  <div class="stat" style="left:207px"><div class="big">1000+</div><b>PROJECTS COMPLETED</b><small>Across residential,<br>commercial &amp;<br>government sectors.</small></div>
  <div class="stat-div" style="left:363px"></div>
  <div class="stat" style="left:391px"><svg width="22" height="24" viewBox="0 0 22 24"><circle cx="11" cy="9" r="6" fill="none" stroke="var(--blue-soft)" stroke-width="2"/><path d="M7 14l-2 8 6-3 6 3-2-8" fill="none" stroke="var(--blue-soft)" stroke-width="2"/></svg><b>PREMIUM MATERIALS</b><small>Aluminium, stainless steel<br>and safety glass built to<br>Australian standards.</small></div>
  <div class="stat-div" style="left:571px"></div>
  <div class="stat" style="left:599px"><svg width="24" height="24" viewBox="0 0 24 24"><circle cx="12" cy="12" r="8" fill="none" stroke="var(--blue-soft)" stroke-width="3" stroke-dasharray="3 2"/><circle cx="12" cy="12" r="3" fill="var(--blue-soft)"/></svg><b>CUSTOM MADE</b><small>Tailored designs to<br>suit your needs<br>and style.</small></div>
  <div class="cta">
    <h3>READY TO START YOUR PROJECT?</h3>
    <p>Get in touch today for a free quote or expert advice.</p>
    <div class="row">
      <span class="btn btn-white">Get a Quote <svg width="13" height="10" viewBox="0 0 14 10"><path d="M0 5h12M8 1l4 4-4 4" stroke="var(--blue)" fill="none" stroke-width="1.5"/></svg></span>
      <span class="btn btn-outline-light"><svg width="12" height="12" viewBox="0 0 24 24"><path fill="#fff" d="M6.6 10.8a15 15 0 006.6 6.6l2.2-2.2c.3-.3.7-.4 1-.2 1.1.4 2.3.6 3.6.6.6 0 1 .4 1 1V20c0 .6-.4 1-1 1A17 17 0 013 4c0-.6.4-1 1-1h3.5c.6 0 1 .4 1 1 0 1.3.2 2.5.6 3.6.1.3 0 .7-.2 1z"/></svg>0400 555 018</span>
    </div>
  </div>
</section>

<section class="serving">
  <h5>PROWEDLY SERVING</h5>
  <div class="row">
    <span><i class="plain-tri"></i>AUSTRALIAN MADE</span>
    <span><svg width="22" height="22" viewBox="0 0 22 22"><circle cx="11" cy="11" r="9.5" fill="none" stroke="var(--blue)" stroke-width="1.5"/><path d="M6.5 11l3 3 6-6" fill="none" stroke="var(--blue)" stroke-width="1.5"/></svg>AS/NZS COMPLIANT</span>
    <span class="wordmark">Korvane<small>POWDER COATINGS</small></span>
    <span><svg width="22" height="22" viewBox="0 0 22 22"><circle cx="11" cy="11" r="9.5" fill="none" stroke="var(--blue)" stroke-width="1.5"/><path d="M4 13c3-2 5 2 8 0s5 0 6 0" fill="none" stroke="var(--blue)" stroke-width="1.5"/></svg>Marine Grade</span>
  </div>
</section>

<section class="about" role="img" aria-label="Glass pool fence with garden and stone paving">
  <div class="intro">
    <div class="eyebrow">ABOUT US</div>
    <h2>DESIGN. FABRICATE. INSTALL.<br><em>DELIVER.</em></h2>
    <div class="rule"></div>
    <p>We are a family-owned and operated business in the Whitsundays, specialising in the design, fabrication and installation of powder coated aluminium, stainless steel and glass products.</p>
    <p>From concept to completion, we take pride in our workmanship and attention to detail.</p>
  </div>
  <span class="btn btn-white">Learn More About Us <svg width="13" height="10" viewBox="0 0 14 10"><path d="M0 5h12M8 1l4 4-4 4" stroke="var(--blue)" fill="none" stroke-width="1.5"/></svg></span>
</section>

<section class="process">
  <h5>OUR PROCESS</h5>
  <h2>QUALITY THROUGH EVERY STEP</h2>
  <div class="steps">
    <div class="step" style="left:145px"><div class="ring"><svg width="28" height="26" viewBox="0 0 28 26"><rect x="2" y="6" width="16" height="12" rx="6" fill="none" stroke="#fff" stroke-width="1.5"/><rect x="12" y="2" width="14" height="10" rx="5" fill="none" stroke="#fff" stroke-width="1.5"/></svg></div><div class="num">01</div><h4>CONSULTATION</h4><p>We listen to your ideas and understand your needs.</p></div>
    <div class="step" style="left:373px"><div class="ring"><svg width="26" height="26" viewBox="0 0 26 26"><path d="M4 22L13 4l9 18M8 14h10" fill="none" stroke="#fff" stroke-width="1.5"/></svg></div><div class="num">02</div><h4>DESIGN</h4><p>Thoughtful, functional designs tailored to your space.</p></div>
    <div class="step" style="left:599px"><div class="ring"><svg width="28" height="22" viewBox="0 0 28 22"><rect x="2" y="6" width="24" height="10" rx="2" fill="none" stroke="#fff" stroke-width="1.5"/><path d="M6 6v10M11 6v10M16 6v10M21 6v10" stroke="#fff" stroke-width="1.2"/></svg></div><div class="num">03</div><h4>FABRICATION</h4><p>Precision manufactured in-house using premium materials.</p></div>
    <div class="step" style="left:826px"><div class="ring"><svg width="26" height="26" viewBox="0 0 26 26"><circle cx="13" cy="13" r="8" fill="none" stroke="#fff" stroke-width="3" stroke-dasharray="3 2"/><circle cx="13" cy="13" r="3" fill="none" stroke="#fff" stroke-width="1.5"/></svg></div><div class="num">04</div><h4>INSTALLATION</h4><p>Expert installation by our experienced team.</p></div>
    <div class="step" style="left:1055px"><div class="ring"><svg width="26" height="26" viewBox="0 0 26 26"><circle cx="13" cy="13" r="10" fill="none" stroke="#fff" stroke-width="1.5"/><path d="M8 13l3.5 3.5L18 10" fill="none" stroke="#fff" stroke-width="1.5"/></svg></div><div class="num">05</div><h4>COMPLETION</h4><p>Built to last with quality you can trust.</p></div>
  </div>
</section>

<section class="vision" role="img" aria-label="Faded view of a hillside garden with stone walls">
  <div class="intro">
    <h2>LET'S BRING YOUR<br><em>VISION TO LIFE.</em></h2>
    <div class="rule"></div>
    <p>Whether it's a custom home, renovation, or large-scale commercial project, we're committed to delivering exceptional craftsmanship from concept to completion. As a family-owned and operated business based in the Whitsundays, we specialise in designing, fabricating, and installing premium powder coated aluminium, stainless steel, and glass products that combine functionality, durability, and contemporary style.</p>
  </div>
  <div class="btns">
    <span class="btn btn-blue"><svg width="18" height="16" viewBox="0 0 18 16"><path d="M2 2h14v9H7l-4 3V11H2z" fill="none" stroke="#fff" stroke-width="1.4"/></svg>GET A QUOTE<svg width="18" height="12" viewBox="0 0 18 12"><path d="M0 6h16M11 1l5 5-5 5" stroke="#fff" fill="none" stroke-width="1.6"/></svg></span>
    <span class="btn btn-outline-blue"><svg width="18" height="16" viewBox="0 0 18 16"><path d="M2 2h14v9H7l-4 3V11H2z" fill="none" stroke="var(--blue)" stroke-width="1.4"/></svg>GET A QUOTE<svg width="18" height="12" viewBox="0 0 18 12"><path d="M0 6h16M11 1l5 5-5 5" stroke="var(--blue)" fill="none" stroke-width="1.6"/></svg></span>
  </div>
  <div class="perks">
    <span><svg width="28" height="24" viewBox="0 0 28 24"><path d="M3 3h22v14H11l-6 4v-4H3z" fill="none" stroke="var(--navy)" stroke-width="1.4"/><path d="M8 9h12M8 13h8" stroke="var(--navy)" stroke-width="1.4"/></svg>FREE QUOTES</span><i></i>
    <span><svg width="22" height="22" viewBox="0 0 22 22"><path d="M5 6a8 8 0 11-1 8" fill="none" stroke="var(--navy)" stroke-width="1.5"/><path d="M5 2v4h4" fill="none" stroke="var(--navy)" stroke-width="1.5"/></svg>QUICK TURNAROUND</span><i></i>
    <span><svg width="22" height="24" viewBox="0 0 22 24"><path d="M11 2l8 3v7c0 5-4 9-8 10-4-1-8-5-8-10V5z" fill="none" stroke="var(--navy)" stroke-width="1.5"/><path d="M7 12l3 3 5-5" fill="none" stroke="var(--navy)" stroke-width="1.5"/></svg>QUALITY GUARANTEE</span>
  </div>
</section>

<footer class="footer">
  <div class="col" style="left:34px;width:210px">
    <div class="fbrand"><span class="dot"></span><div>BRELLAN COATWORKS<small>MACKABY</small></div></div>
    <div class="rule"></div>
    <p>We are a family business based in the Whitsundays, specialising in the design, fabrication and installation of powder coated aluminium, stainless steel and glass products.</p>
    <p style="margin-top:14px">Proudly servicing from Airlie Beach to Townsville and surrounding areas.</p>
    <div class="socials"><i></i><i></i><i></i></div>
  </div>
  <div class="fdiv" style="left:290px"></div>
  <div class="col" style="left:316px">
    <h4>SERVICING</h4>
    <ul class="flinks">
      <li>Privacy Screens<span>›</span></li>
      <li>Balustrades<span>›</span></li>
      <li>Glass Fencing<span>›</span></li>
      <li>Stainless Steel HandrailsP<span>›</span></li>
      <li>owder Coated Aluminium Handrails<span>›</span></li>
      <li>Pool Fencing &amp; Gates<span>›</span></li>
    </ul>
    <span class="btn btn-outline-light" style="margin-top:58px;border-color:var(--blue-soft);color:var(--blue-soft);height:37px">View All Products <svg width="13" height="10" viewBox="0 0 14 10"><path d="M0 5h12M8 1l4 4-4 4" stroke="var(--blue-soft)" fill="none" stroke-width="1.5"/></svg></span>
  </div>
  <div class="fdiv" style="left:574px"></div>
  <div class="col" style="left:599px">
    <h4>SERVICING</h4>
    <p style="margin-top:34px">Proudly servicing from Airlie Beach to<br>Townsville and surrounding areas.</p>
    <div class="map" role="img" aria-label="Coastal map from Townsville to Airlie Beach with service locations"></div>
  </div>
  <div class="fdiv" style="left:858px"></div>
  <div class="col" style="left:883px">
    <h4>CONTACT US</h4>
    <ul class="fcontact" style="margin-top:34px">
      <li><svg width="18" height="18" viewBox="0 0 24 24"><path fill="none" stroke="#fff" stroke-width="1.5" d="M6.6 10.8a15 15 0 006.6 6.6l2.2-2.2c.3-.3.7-.4 1-.2 1.1.4 2.3.6 3.6.6.6 0 1 .4 1 1V20c0 .6-.4 1-1 1A17 17 0 013 4c0-.6.4-1 1-1h3.5c.6 0 1 .4 1 1 0 1.3.2 2.5.6 3.6.1.3 0 .7-.2 1z"/></svg><span style="font-size:14px">0400 555 018</span></li>
      <li><svg width="18" height="14" viewBox="0 0 26 20"><rect x="1" y="1" width="24" height="18" rx="2" fill="none" stroke="#fff" stroke-width="2"/><path d="M1 2l12 9 12-9" fill="none" stroke="#fff" stroke-width="2"/></svg>info@brellancoatworks.com.au</li>
      <li><svg width="16" height="20" viewBox="0 0 20 26"><path d="M10 1a8 8 0 018 8c0 6-8 16-8 16S2 15 2 9a8 8 0 018-8z" fill="none" stroke="#fff" stroke-width="1.8"/><circle cx="10" cy="9" r="3" fill="none" stroke="#fff" stroke-width="1.8"/></svg>Mackaby, QLD 4790</li>
    </ul>
    <h4 style="margin-top:44px">BUSINESS HOURS</h4>
    <div class="rule" style="margin:14px 0 16px"></div>
    <p>Monday – Friday : 7:00am – 4:00pm<br>Saturday - By Appointment</p>
    <span class="btn btn-outline-light" style="margin-top:34px;border-color:var(--blue-soft);color:var(--blue-soft);height:37px">GET A QUOTE <svg width="13" height="10" viewBox="0 0 14 10"><path d="M0 5h12M8 1l4 4-4 4" stroke="var(--blue-soft)" fill="none" stroke-width="1.5"/></svg></span>
  </div>
</footer>

<section class="badges">
  <span><i class="plain-tri"></i>AUSTRALIAN MADE</span>
  <span><svg width="30" height="30" viewBox="0 0 30 30"><circle cx="15" cy="15" r="13" fill="none" stroke="var(--navy)" stroke-width="1.8"/><path d="M9 15l4 4 8-8" fill="none" stroke="var(--navy)" stroke-width="1.8"/></svg>AS/NZS COMPLIANT</span>
  <span class="wordmark" style="font-size:20px">Korvane<small style="font-size:11px;color:var(--navy)">POWDER COATINGS</small></span>
  <span><svg width="30" height="30" viewBox="0 0 30 30"><circle cx="15" cy="15" r="13" fill="none" stroke="var(--navy)" stroke-width="1.8"/><path d="M5 17c4-3 7 3 11 0s7 0 9 0" fill="none" stroke="var(--navy)" stroke-width="1.8"/></svg>MARINE GRADE</span>
  <span><svg width="26" height="30" viewBox="0 0 26 30"><path d="M13 2l10 4v9c0 7-5 11-10 13-5-2-10-6-10-13V6z" fill="none" stroke="var(--navy)" stroke-width="1.8"/><path d="M8 15l3.5 3.5L18 12" fill="none" stroke="var(--navy)" stroke-width="1.8"/></svg>PREMIUM MATERIALS</span>
  <span><svg width="30" height="30" viewBox="0 0 30 30"><path d="M5 25L25 5M5 5l20 20" stroke="var(--navy)" stroke-width="2"/></svg>EXPERT CRAFTSMANSHIP</span>
</section>

<div class="copy">
  <span>© Brellan Coatworks Mackaby. All Rights Reserved.</span>
  <div class="links"><span>Privacy Policy</span><i></i><span>Terms &amp; Conditions</span><i></i><span>Sitemap</span></div>
</div>

</div>
</body>
</html>
```